Personal Training Business at home (Brook Vitality & Health)

My business name will be Brook Vitality & Health and will be training people with special needs (Asthma, Diabetes, Obesity, Rehab, Sports Performance) for all ages. It will be set indoor and outdoor for all types of weather conditions. I,m also doing Pilates group classes as well in a Japanese garden setting.I will be working alone so the groups will be small and the client has a high quality of service. I just need something very basic to start with then as the business expands I can edit it to it,s growth.

Target Market(s)

Target special population persons with dysfunctions injuries, metabolic/cardio-respiratory conditions, sports performance and more also healthy food choices.

Industry/Entity Type

Business

Number of Pages Required

3 page

Font styles to use
Serif

Colors
f78f20
ffffff
474747
cbcbcb
abd036

Requirements
Must have
• The website must have accessibility for change, to be able to link on other networks like my own ClipHarbor videos. A basic lay out so I can fill in the pages and ad more as I expand the business. The logo to have the A for Brook to be an image of a man shaped as the letter A with his arms extended out/up. Private Facility and must ring for appointment to enter premises.
Nice to have
• The Image I want to have in my studio is for people to be serious about training & health choices. I want them to be able to train in a comfortable environment and free of air conditioned concrete rooms with machines. My home is converted to a Organic feature and outdoor/indoor training facility that my clients & I can share the natural freedom of training in the elements. My client have special needs and need extra care, they are people with injuries, metabolic/cardio-respiratory condition, asthmatics & more they need to be screened and tested for the condition that they suffer from and together with there allied professional we work together to treat them with the up most care for maximum results. This is what I want to target I long term client with real Goals on there mind and not some pipe dream.
Should not have
• Not to be portray as a Gym with machines and clients that only care about image.

```html
<!DOCTYPE html>
<html lang="en">
<head>
<meta charset="utf-8">
<title>Brook Fitness</title>
<link href="https://fonts.googleapis.com/css2?family=Open+Sans:wght@400;600&display=swap" rel="stylesheet">
<style>
:root{
  --orange:#f78f20;
  --green:#9bbd35;
  --dark:#474747;
  --darker:#3a3a3a;
  --grey-band:#efefef;
  --text:#555;
  --white:#fff;
  --line:#cbcbcb;
}
*{margin:0;padding:0;box-sizing:border-box}
html,body{width:817px;height:1200px;overflow:hidden}
body{font-family:"Open Sans",sans-serif;color:var(--text);background:var(--white);position:relative}
.wrap{width:636px;margin:0 auto;position:relative}
.topbar{height:54px;background:var(--orange)}
.topbar .wrap{height:54px;display:flex;align-items:center;justify-content:space-between}
.brand{color:var(--white);font-size:22px;font-weight:600}
.contacts{display:flex;gap:18px}
.contact{display:flex;align-items:center;gap:6px;color:var(--white);text-align:right}
.contact small{display:block;font-size:8px;line-height:1}
.contact span{font-size:11.5px;line-height:1.2}
.contact svg{width:20px;height:20px}
.mainnav{height:28px;background:var(--dark)}
.mainnav ul{list-style:none;display:flex;height:28px;border-left:1px solid var(--darker)}
.mainnav li{font-size:7.5px;color:#ddd;padding:0 15.5px;line-height:28px;border-right:1px solid var(--darker)}
.mainnav li.current{background:#2f2f2f;color:var(--white);padding:0 18px}
.hero{height:272px;background:linear-gradient(160deg,#9a6a45 0%,#b5774a 45%,#8a5a38 100%);position:relative}
.hero-caption{position:absolute;left:511px;top:116px;width:215px;background:rgba(255,255,255,.85);padding:8px 10px;text-align:right;font-size:13.5px;line-height:1.35;color:#222}
.dots{position:absolute;left:382px;top:245px;display:flex;gap:4px;background:rgba(0,0,0,.35);padding:2px 4px;border-radius:6px}
.dots i{width:6px;height:6px;border-radius:50%;background:var(--white);display:block}
.dots i:first-child{background:transparent;border:1px solid var(--white)}
.welcome{height:124px;text-align:center;padding-top:28px}
.welcome h1{font-size:18px;font-weight:400;color:var(--green);margin-bottom:6px}
.welcome p{font-size:7.2px;line-height:14px}
.services{height:180px;background:var(--grey-band);padding-top:16px}
.services .wrap{display:flex;gap:18px}
.video{width:160px;height:147px;border:3px solid var(--white);background:linear-gradient(180deg,#f7b24a,#e86a1e 60%,#8a3a12);flex:none}
.services h2{font-size:19px;font-weight:400;color:var(--orange);margin:-2px 0 10px}
.services p{font-size:7.2px;line-height:14px;margin-bottom:8px}
.svc-list{display:grid;grid-template-columns:168px 160px;list-style:none;font-size:8.3px;color:#333;row-gap:5px;grid-auto-flow:column;grid-template-rows:repeat(4,13px)}
.svc-list li::before{content:"•";margin-right:6px}
.needs{height:178px;padding-top:30px}
.needs h2{text-align:center;font-size:15.8px;letter-spacing:-.25px;font-weight:400;color:var(--green);line-height:24px;margin:0 -4px 20px}
.needs h2 b{font-weight:600}
.cred{display:grid;grid-template-columns:242px 221px 173px;font-size:8.3px;color:#333;line-height:13px}
.cred ul{list-style:none}
.cred ul:nth-child(2){max-width:172px}
.cred li{padding-left:8px;text-indent:-8px;margin-bottom:8px}
.cred li::before{content:"•";margin-right:4px}
.areas{height:288px;background:var(--grey-band);padding-top:26px}
.areas .wrap{display:grid;grid-template-columns:repeat(3,196px);column-gap:23px}
.area{position:relative;height:262px}
.area-photo{height:108px}
.p-garden{background:linear-gradient(180deg,#6f5a4a,#4d5a30 60%,#7a5a4a)}
.p-group{background:linear-gradient(180deg,#7ca24a,#c6b86a 55%,#94b04a)}
.p-deck{background:linear-gradient(180deg,#4b4a3c,#8a6a50 40%,#6f5140)}
.area h3{font-size:11px;font-weight:600;color:#222;margin:13px 0 5px;line-height:14px}
.area p{font-size:6px;line-height:11px;color:#666;text-align:justify}
.more{position:absolute;left:0;top:229px;font-size:6.8px;color:#777;border:1px solid var(--line);background:var(--white);padding:6px 8px}
.footer{height:76px;background:var(--dark);padding-top:24px}
.footer .wrap{display:flex;justify-content:space-between}
.footnav{list-style:none;display:flex;font-size:6.8px;color:#ccc}
.footnav li+li::before{content:"|";margin:0 7px;color:#888}
.copy{font-size:6.8px;color:#bbb;margin-top:11px}
.social{display:flex;gap:4px;margin-top:6px}
.social i{width:17px;height:17px;border-radius:50%;display:block}
.social .s-one{background:#3b5a9a}
.social .s-two{background:#2fa9e0}
</style>
</head>
<body>
<header class="topbar">
  <div class="wrap">
    <div class="brand">Brook Fitness</div>
    <div class="contacts">
      <div class="contact"><div><small>Email</small><span>brookfithealth@mailnest.com</span></div>
        <svg viewBox="0 0 20 20"><circle cx="10" cy="10" r="10" fill="#fff"/><rect x="5.5" y="6.5" width="9" height="7" rx="1" fill="#f78f20"/><path d="M5.8 7l4.2 3.5L14.2 7" stroke="#fff" stroke-width="1" fill="none"/></svg></div>
      <div class="contact"><div><small>Mobile</small><span>0491570156</span></div>
        <svg viewBox="0 0 20 20"><circle cx="10" cy="10" r="10" fill="#fff"/><path d="M7 5.5l2 2-1 1.2c.6 1.4 1.7 2.5 3.1 3.1l1.2-1 2 2-1.3 1.5C10 14 6 10 5.6 6.8z" fill="#f78f20"/></svg></div>
    </div>
  </div>
</header>
<nav class="mainnav">
  <div class="wrap">
    <ul>
      <li class="current">Home</li><li>About BROOK FIT &amp; HEALTH</li><li>Trading Hours</li><li>Pricing &amp; Packages</li><li>Trainers Profile Leon Marsh</li><li>Trainings</li><li>Contact us</li>
    </ul>
  </div>
</nav>
<section class="hero" role="img" aria-label="Wooden deck with a potted jade plant">
  <div class="hero-caption">Phasellus nisl est<br>condimentum vitae faucibus</div>
  <div class="dots"><i></i><i></i><i></i><i></i></div>
</section>
<section class="welcome">
  <div class="wrap">
    <h1>Welcome to Brook Fitness</h1>
    <p>All my life I have been looking for a place that I can train in a comfortable and natural environment instead been surrounded by concrete walls &amp; floors, what I am offering in my studio gym is a natural organic style of training that clients can feel whatit's like to be outside in the elements. This is something that you can come feel &amp; enjoy the pleasure of training in the outdoors and still accomplishing your goals.</p>
  </div>
</section>
<section class="services">
  <div class="wrap">
    <div class="video" role="img" aria-label="ClipHarbor video: woman meditating at sunset"></div>
    <div>
      <h2>Training services</h2>
      <p>The business is constantly staying intouch with newest concepts by upgrading the knowledge and qualifications that are available to trainers to make sure that you get the benefits and most important is not to getting injured.</p>
      <ul class="svc-list">
        <li>Personal training one on one</li><li>Group functional training</li><li>Sports performance</li><li>Pilates</li>
        <li>Recovery &amp; stretching classes</li><li>Rehabilitation programs</li><li>Basic lifestyle choice plans</li>
      </ul>
    </div>
  </div>
</section>
<section class="needs">
  <div class="wrap">
    <h2>We are training people with special needs <b>(Asthma, Diabetes, Obesity, Rehab, Sports Performance)</b> for all ages</h2>
    <div class="cred">
      <ul><li>Diploma in fitness (Fernvale institute of fitness)</li><li>Advanced First Aid&nbsp; certification</li></ul>
      <ul><li>Basic nutrition certification</li><li>Vast experience in injury and recover rehabilitation exercises Fascia release</li></ul>
      <ul><li>Experience in mind body meditation and neuromuscular release</li><li>30 years experience in customer service</li></ul>
    </div>
  </div>
</section>
<section class="areas">
  <div class="wrap">
    <article class="area">
      <div class="area-photo p-garden" role="img" aria-label="Bonsai garden with trees on wooden stands"></div>
      <h3>Facilities Equipment and Environment</h3>
      <p>Pilate'sorganic area can accommodate 4-6 people at anytime comfortably in a tranquil Japanese Garden setting that is Pilates and goes hand in hand for a unique experience and you will be satisfied with the outcome, the connection with your mind &amp; body will feel re-energized and charged.</p>
      <span class="more">Read more</span>
    </article>
    <article class="area">
      <div class="area-photo p-group" role="img" aria-label="Group exercising outdoors on grass"></div>
      <h3>Group Training Section</h3>
      <p>This area can accommodate 4-6 people at a time comfortably with a beautiful surrounding of a Japanese influenced garden. We have a combination of equipment like Kettle Bells, Dumbbells, Battle ropes, Climbing wall, skipping ropes, hanging ropes, Olympic lifting bars, Tire flipping, Sled pulling,&amp; more.</p>
      <span class="more">Read more</span>
    </article>
    <article class="area">
      <div class="area-photo p-deck" role="img" aria-label="Timber deck in a garden area"></div>
      <h3>Wellbeing &amp; Spiritual Area</h3>
      <p>Enjoy the pleasant surroundings with a cool drink in Summer or warm tea in Winter in the beautiful Bonsai Garden that you can Meditate &amp; connect with your mind and body by selecting a Bonsai of your choice and recharge with the natural energy it releases, and combined with an incense that you choose you will feel one with yourself and restore your spiritual charge.</p>
      <span class="more">Read more</span>
    </article>
  </div>
</section>
<footer class="footer">
  <div class="wrap">
    <div>
      <ul class="footnav"><li>Home</li><li>About BROOK FIT &amp; HEALTH</li><li>Trading Hours</li><li>Pricing &amp; Packages</li><li>Trainers Profile Leon Marsh</li><li>Trainings</li><li>Contact us</li></ul>
      <p class="copy">Copyright ©&nbsp; 2016&nbsp; Brook Fitness.&nbsp; All rights reserved</p>
    </div>
    <div class="social"><i class="s-one"></i><i class="s-two"></i></div>
  </div>
</footer>
</body>
</html>
```